Interior Design/ New Construction interior finishes

Interior Design Website

Target Market(s)

Home builders, New Construction, Renovations, Public

Industry/Entity Type

Construction

Coding

Coded - Design and coding required

Number of Pages Required

1 page

Font styles to use
Sans Serif

Colors

Designer to choose colors to be used in the design.

Requirements
Must have
• Section to upload pictures of projects
• Simple and modern design
• Designer 1 details about myself
• Logo
• Upload section for photos for future jobs
Nice to have
• Sections they can click on to see certain rooms in a house
• Decorating, floral arrangements, holiday decorating.
• I have lots of before and after as well. Maybe a section for those.

```html
<!DOCTYPE html>
<html lang="en">
<head>
<meta charset="utf-8">
<title>Verra Interiors</title>
<link href="https://fonts.googleapis.com/css2?family=Montserrat:wght@400;600;700&family=Raleway:wght@400;500;600;700&display=swap" rel="stylesheet">
<style>
:root{
  --orange:#f7891d;
  --blue:#3aa6e8;
  --ink:#2b2b2b;
  --body:#555;
  --white:#fff;
  --light:#f0f0f0;
  --card:#fafafa;
  --footer:#1c1c1c;
}
*{margin:0;padding:0;box-sizing:border-box}
html,body{width:1200px;height:3180px;overflow:hidden}
body{font-family:'Raleway',sans-serif;color:var(--body);background:var(--white);position:relative}
section,header,footer{position:absolute;left:0;width:1200px}
.abs{position:absolute}
.btn{position:absolute;background:var(--orange);color:var(--white);font-family:'Montserrat',sans-serif;font-weight:600;font-size:12px;letter-spacing:.5px;text-transform:uppercase;display:flex;align-items:center;justify-content:center}
.photo{position:absolute}
.section-title{position:absolute;left:0;width:1200px;text-align:center;font-family:'Raleway',sans-serif;font-weight:500;font-size:22px;letter-spacing:.5px;text-transform:uppercase;color:var(--ink)}

/* hero */
.hero{top:0;height:598px;background:linear-gradient(180deg,#5b5650 0%,#6f6a63 35%,#4d4a47 70%,#3e3c3c 100%)}
.hero-shade{position:absolute;inset:0;background:linear-gradient(90deg,rgba(30,30,30,.35),rgba(30,30,30,.15) 60%,rgba(30,30,30,.35))}
.contact-label{font-family:'Montserrat',sans-serif;font-size:13px;color:var(--orange);text-transform:uppercase;letter-spacing:.3px}
.contact-value{font-family:'Montserrat',sans-serif;font-weight:600;color:var(--white)}
.brand{position:absolute;left:509px;top:0;width:182px;height:131px}
.brand-name{position:absolute;left:0;width:182px;top:70px;text-align:center;font-family:'Raleway',sans-serif;font-size:20px;font-weight:500;color:var(--ink);letter-spacing:1px}
.hero-kicker{left:161px;top:218px;font-family:'Montserrat',sans-serif;font-size:22px;color:var(--orange);text-transform:uppercase;letter-spacing:.3px}
.hero-title{left:161px;top:252px;font-family:'Montserrat',sans-serif;font-weight:700;font-size:42px;line-height:46px;color:var(--white);text-transform:uppercase}
.hero-sub{left:161px;top:358px;font-family:'Montserrat',sans-serif;font-size:17px;line-height:23px;color:var(--white)}
.video{left:615px;top:216px;width:424px;height:261px;border:4px solid rgba(255,255,255,.35);background:linear-gradient(160deg,#d8a560 0%,#a56e35 40%,#6e4a2c 75%,#8d7a66 100%)}
.play{position:absolute;left:182px;top:100px}

/* about */
.about{top:598px;height:458px;background:var(--white)}
.about h2{position:absolute;left:161px;top:82px;font-weight:500;font-size:22px;color:var(--ink);text-transform:uppercase;letter-spacing:.3px}
.about .lead{position:absolute;left:161px;top:140px;width:440px;font-size:11px;line-height:19px;font-weight:700;color:var(--ink)}
.about .copy{position:absolute;left:161px;top:182px;width:440px;font-size:11px;line-height:19.5px;color:var(--body)}
.team{left:632px;top:102px;width:407px;height:265px;background:radial-gradient(ellipse at 50% 40%,#d9dce0 0%,#c4c8cd 50%,#f5f5f5 95%)}

/* services */
.services{top:1056px;height:526px;background:linear-gradient(180deg,#3b3b3b 0%,#2e2e2e 60%,#242424 100%)}
.services .section-title{top:76px;color:var(--white)}
.service{position:absolute;top:162px;width:300px;text-align:center}
.ring{position:absolute;left:76px;top:0;width:148px;height:148px;border:2px solid var(--blue);border-radius:50%}
.ring svg{position:absolute;left:44px;top:44px}
.badge{position:absolute;left:195px;top:8px;width:30px;height:30px;border-radius:50%;background:var(--orange);border:3px solid var(--white);color:var(--white);font-family:'Montserrat',sans-serif;font-weight:700;font-size:14px;display:flex;align-items:center;justify-content:center}
.service h3{position:absolute;top:178px;left:0;width:300px;font-family:'Montserrat',sans-serif;font-weight:700;font-size:12.5px;color:var(--white);text-transform:uppercase}
.service p{position:absolute;top:210px;left:40px;width:220px;font-size:11px;line-height:20px;color:#c9c9c9}

/* projects */
.projects{top:1582px;height:506px;background:var(--white)}
.projects .section-title{top:80px}
.project{position:absolute;top:152px;width:218px}
.project .photo{position:relative;width:218px;height:157px}
.project h4{margin-top:12px;text-align:center;font-family:'Montserrat',sans-serif;font-weight:700;font-size:11px;color:var(--ink);text-transform:uppercase}
.project p{margin-top:6px;text-align:center;font-size:10.5px;line-height:16px;color:var(--body)}
.project .more{display:block;margin-top:6px;text-align:center;font-size:9.5px;font-weight:700;color:var(--orange);text-transform:uppercase}

/* testimonials */
.testimonials{top:2088px;height:473px;background:var(--light)}
.testimonials .section-title{top:82px}
.quote-card{position:absolute;top:191px;width:428px;height:201px;background:var(--card)}
.avatar{position:absolute;left:178px;top:-36px;width:72px;height:72px;border-radius:50%;border:4px solid var(--white);background:linear-gradient(180deg,#b9b3ad,#8f8a86)}
.quote-card p{position:absolute;left:40px;top:60px;width:348px;text-align:center;font-size:11px;line-height:20px;color:var(--ink)}
.quote-card .name{position:absolute;left:0;width:428px;top:156px;text-align:center;font-family:'Montserrat',sans-serif;font-weight:600;font-size:11px;color:var(--blue);text-transform:uppercase}
.qmark{position:absolute;font-family:Georgia,serif;font-size:46px;line-height:1;color:#dcdcdc}

/* contact */
.contact{top:2561px;height:540px;background:linear-gradient(180deg,#3a2c22 0%,#4a3a2e 40%,#2c241f 100%)}
.contact-shade{position:absolute;inset:0;background:rgba(20,18,16,.45)}
.contact .section-title{top:80px;color:var(--white)}
.contact .intro{position:absolute;left:0;width:1200px;top:147px;text-align:center;font-size:13px;color:var(--white)}
.field{position:absolute;left:439px;width:322px;height:38px;background:var(--white);font-size:10.5px;color:#888;padding-left:18px;display:flex;align-items:center}
.field svg{position:absolute;right:16px;top:16px}

footer{top:3101px;height:79px;background:var(--footer)}
footer .legal{position:absolute;left:161px;top:32px;font-size:11px;color:#777}
footer .legal b{color:var(--orange);font-weight:500}
.social{position:absolute;top:31px;width:16px;height:16px;border-radius:50%;background:#666}
</style>
</head>
<body>

<header class="hero">
  <div class="photo" style="inset:0" role="img" aria-label="Bright living room interior with sofas and armchairs"></div>
  <div class="hero-shade"></div>

  <div class="abs contact-label" style="left:235px;top:30px">Email us on</div>
  <div class="abs contact-value" style="left:161px;top:52px;font-size:25px">hello@verrainteriors.com</div>

  <svg class="brand" width="182" height="131" viewBox="0 0 182 131" aria-hidden="true">
    <path d="M0 0H182V112Q91 140 0 112Z" fill="#fff"/>
    <circle cx="91" cy="36" r="18" fill="none" stroke="#2b2b2b" stroke-width="2"/>
  </svg>
  <div class="brand"><div class="brand-name">Verra Interiors</div></div>

  <div class="abs contact-label" style="left:866px;top:30px">Get started today</div>
  <div class="abs contact-value" style="left:826px;top:50px;font-size:29px">5555 0101 2323</div>

  <div class="abs hero-kicker">Lorem ipsum dolor sit</div>
  <h1 class="abs hero-title">Consectetur<br>Adipiscing</h1>
  <p class="abs hero-sub">Sed ut perspiciatis unde omnis<br>iste natus error sit volu.</p>
  <div class="btn" style="left:161px;top:430px;width:172px;height:45px">Get started</div>

  <div class="photo video" role="img" aria-label="Warmly lit open-plan lounge with sofa and glass doors, video preview">
    <svg class="play" width="44" height="44" viewBox="0 0 44 44" aria-hidden="true">
      <circle cx="22" cy="22" r="20" fill="#fff" opacity=".9"/>
      <path d="M17 13L31 22L17 31Z" fill="#2b2b2b"/>
    </svg>
  </div>
</header>

<section class="about">
  <h2>About our company</h2>
  <p class="lead">Lorem ipsum dolor sit amet, consectetur adipiscing elit, sed do eiusmod tempor incididunt ut labore et dolore magna aliqua.</p>
  <p class="copy">Lorem ipsum dolor sit amet, consectetur adipiscing elit, sed do eiusmod tempor incididunt ut labore et dolore magna aliqua. Ut enim ad minim veniam, quis nostrud exercitation ullamco laboris nisi ut aliquip ex ea commodo consequat. Duis aute irure dolor in reprehenderit in voluptate velit esse cillum dolore eu fugiat nulla pariatur. Lorem ipsum dolor sit amet, consectetur adipiscing elit, sed do eiusmod tempor incididunt ut labore et dolore magna aliqua. Lorem ipsum dolor sit amet, consectetur adipiscing elit, sed do eiusmod tempor incididunt ut labore.</p>
  <div class="btn" style="left:161px;top:339px;width:151px;height:36px;font-size:11px">Learn more</div>
  <div class="photo team" role="img" aria-label="Three team members in hard hats and business attire"></div>
</section>

<section class="services">
  <div class="photo" style="inset:0" role="img" aria-label="Dim modern kitchen interior in the background"></div>
  <div class="section-title">Our services</div>

  <div class="service" style="left:147px">
    <div class="ring">
      <svg width="60" height="60" viewBox="0 0 60 60" fill="none" stroke="#3aa6e8" stroke-width="3" aria-hidden="true">
        <path d="M30 12H14a3 3 0 0 0-3 3v31a3 3 0 0 0 3 3h31a3 3 0 0 0 3-3V30"/>
        <path d="M44 9l7 7-20 20-9 2 2-9z"/>
      </svg>
    </div>
    <div class="badge">1</div>
    <h3>Do this thing</h3>
    <p>Lorem ipsum dolor sit amet, con etur adipiscing elit, sed do eiusmod tempor incididunt ut labore et dolore magna aliqua. Ut enimminim.</p>
  </div>

  <div class="service" style="left:450px">
    <div class="ring">
      <svg width="60" height="60" viewBox="0 0 60 60" aria-hidden="true">
        <rect x="13" y="8" width="34" height="44" rx="3" fill="#3aa6e8"/>
        <rect x="18" y="13" width="24" height="8" fill="#2e2e2e"/>
        <g fill="#2e2e2e">
          <rect x="18" y="26" width="6" height="5"/><rect x="27" y="26" width="6" height="5"/><rect x="36" y="26" width="6" height="5"/>
          <rect x="18" y="34" width="6" height="5"/><rect x="27" y="34" width="6" height="5"/><rect x="36" y="34" width="6" height="5"/>
          <rect x="18" y="42" width="6" height="5"/><rect x="27" y="42" width="6" height="5"/><rect x="36" y="42" width="6" height="5"/>
        </g>
      </svg>
    </div>
    <div class="badge">2</div>
    <h3>Then do this</h3>
    <p>Lorem ipsum dolor sit amet, con etur adipiscing elit, sed do eiusmod tempor incididunt ut labore et dolore magna aliqua. Ut enimminim.</p>
  </div>

  <div class="service" style="left:749px">
    <div class="ring">
      <svg width="60" height="60" viewBox="0 0 60 60" aria-hidden="true">
        <path d="M30 8L5 30h7v22h13V38h10v14h13V30h7z" fill="#3aa6e8"/>
      </svg>
    </div>
    <div class="badge">3</div>
    <h3>Then this thing</h3>
    <p>Lorem ipsum dolor sit amet, con etur adipiscing elit, sed do eiusmod tempor incididunt ut labore et dolore magna aliqua. Ut enimminim.</p>
  </div>
</section>

<section class="projects">
  <div class="section-title">Our laest projects</div>

  <article class="project" style="left:161px">
    <div class="photo" style="background:linear-gradient(160deg,#c9a27a,#8a5a36 60%,#5a3c28)" role="img" aria-label="Open kitchen and dining area with timber ceiling"></div>
    <h4>Lorem ipsum dolor sit amet</h4>
    <p>Consectetur adipiscing elit, sed do eu mod tempor incididunt ut labore et dolore magna aliqua. Ut enim ad minim veniam, quis nostrud exercitation ullamco laboris nisi ut.</p>
    <span class="more">Read more</span>
  </article>

  <article class="project" style="left:383px">
    <div class="photo" style="background:linear-gradient(160deg,#b7aba0,#6d6259 60%,#3f3833)" role="img" aria-label="Modern dining room with chandelier"></div>
    <h4>Duis aute irure reprehenderit</h4>
    <p>Consectetur adipiscing elit, sed do eu mod tempor incididunt ut labore et dolore magna aliqua. Ut enim ad minim veniam, quis nostrud exercitation ullamco laboris nisi ut.</p>
    <span class="more">Read more</span>
  </article>

  <article class="project" style="left:604px">
    <div class="photo" style="background:linear-gradient(170deg,#cfc8c0,#8f1f22 60%,#5c2a22)" role="img" aria-label="Home games room with red carpet and basketball hoop"></div>
    <h4>Nemo enim ipsam voluptatem</h4>
    <p>Consectetur adipiscing elit, sed do eu mod tempor incididunt ut labore et dolore magna aliqua. Ut enim ad minim veniam, quis nostrud exercitation ullamco laboris nisi ut.</p>
    <span class="more">Read more</span>
  </article>

  <article class="project" style="left:822px">
    <div class="photo" style="background:linear-gradient(160deg,#d7b48c,#9a6a45 55%,#6a4a35)" role="img" aria-label="Living room with tall windows and fireplace"></div>
    <h4>Quis autem vel reprehenderit</h4>
    <p>Consectetur adipiscing elit, sed do eu mod tempor incididunt ut labore et dolore magna aliqua. Ut enim ad minim veniam, quis nostrud exercitation ullamco laboris nisi ut.</p>
    <span class="more">Read more</span>
  </article>
</section>

<section class="testimonials">
  <div class="section-title">Our client says</div>

  <div class="quote-card" style="left:161px">
    <div class="avatar" role="img" aria-label="Portrait of client Ellis Hart"></div>
    <span class="qmark" style="left:20px;top:18px">&ldquo;</span>
    <p>Lorem ipsum dolor sit amet, con etur adipiscing elit, sed do eiusmod tempor incididunt ut labore et dolore magna aliqua. Ut enimminim veniam, quis nostrud exercitation ullamco laboris nisi ut aliquip ex ea commodo consequat.</p>
    <div class="name">Ellis Hart</div>
    <span class="qmark" style="right:20px;top:150px">&rdquo;</span>
  </div>

  <div class="quote-card" style="left:611px">
    <div class="avatar" role="img" aria-label="Portrait of client Owen Pike"></div>
    <span class="qmark" style="left:20px;top:18px">&ldquo;</span>
    <p>Lorem ipsum dolor sit amet, con etur adipiscing elit, sed do eiusmod tempor incididunt ut labore et dolore magna aliqua. Ut enimminim veniam, quis nostrud exercitation ullamco laboris nisi ut aliquip ex ea commodo consequat.</p>
    <div class="name">Owen Pike</div>
    <span class="qmark" style="right:20px;top:150px">&rdquo;</span>
  </div>
</section>

<section class="contact">
  <div class="photo" style="inset:0" role="img" aria-label="Blurred great room with stone fireplace and large windows"></div>
  <div class="contact-shade"></div>
  <div class="section-title">Contact us</div>
  <div class="intro">Fill up the following information</div>
  <div class="field" style="top:189px">Name</div>
  <div class="field" style="top:242px">Email</div>
  <div class="field" style="top:295px">Phone</div>
  <div class="field" style="top:348px">Sate / Province
    <svg width="10" height="6" viewBox="0 0 10 6" aria-hidden="true"><path d="M0 0h10L5 6z" fill="#333"/></svg>
  </div>
  <div class="btn" style="left:439px;top:409px;width:322px;height:47px">Submit now</div>
</section>

<footer>
  <div class="legal">&copy; Copyright <b>Verra Interiors</b>. All Rights Reserved.</div>
  <span class="social" style="left:900px"></span>
  <span class="social" style="left:936px"></span>
  <span class="social" style="left:972px"></span>
  <span class="social" style="left:1014px"></span>
</footer>

</body>
</html>
```